Energy trading company (Voltrisa) needs a business card

We need a business card for a company based in Central America. Our main purpose is trading energy . We already have the logo but we need some good creativity to design a high impact business card. Colors blue, orange, green can be used or we would like to see good combinatios with our logo

Target Market(s)

Energy

Industry/Entity Type

Power Generation

Contact Information for Business Card

Logo , headquarters , name, background

Font styles to use
Serif
Sans Serif

Colors

Designer to choose colors to be used in the design.

Requirements
Must have
• it must have a fresh and clean view
Nice to have
• good backgrounds that combine with the logo
Should not have
• too much words

```html
<!DOCTYPE html>
<html lang="en">
<head>
<meta charset="utf-8">
<title>Voltrisa Business Card</title>
<link rel="stylesheet" href="https://fonts.googleapis.com/css2?family=Questrial&family=Lato:wght@400;700&display=swap">
<style>
  :root {
    --navy: #2f5877;
    --navy-deep: #264a66;
    --navy-light: #3a6788;
    --orange: #f39325;
    --green: #9fcf63;
    --paper: #ffffff;
    --ink: #2c4a63;
    --backdrop: #e6e8eb;
  }
  * { margin: 0; padding: 0; box-sizing: border-box; }
  html, body { width: 1200px; height: 900px; overflow: hidden; }
  body {
    background: var(--backdrop);
    display: flex;
    align-items: center;
    justify-content: center;
    gap: 60px;
    font-family: "Questrial", "Lato", sans-serif;
  }
  .card {
    position: relative;
    width: 520px;
    height: 298px;
    overflow: hidden;
    box-shadow: 0 6px 18px rgba(0,0,0,0.18);
  }
  /* Front */
  .card-front { background: var(--paper); }
  .card-front .decor { position: absolute; inset: 0; }
  .front-info { position: absolute; left: 34px; top: 30px; }
  .brand-name {
    color: var(--orange);
    font-size: 34px;
    letter-spacing: 0.5px;
    text-transform: uppercase;
    line-height: 1;
  }
  .person-name {
    margin-top: 14px;
    color: var(--ink);
    font-family: "Lato", sans-serif;
    font-weight: 700;
    font-size: 17px;
    letter-spacing: 1px;
    text-transform: uppercase;
  }
  .contact-list { list-style: none; margin-top: 16px; }
  .contact-list li {
    display: flex;
    align-items: center;
    gap: 9px;
    color: var(--ink);
    font-size: 14px;
    line-height: 22px;
  }
  .contact-list svg { width: 12px; height: 12px; fill: var(--orange); flex: none; }
  .address {
    position: absolute;
    left: 34px;
    bottom: 28px;
    color: var(--orange);
    font-size: 15px;
  }
  /* Back */
  .card-back {
    background: radial-gradient(circle at 55% 45%, var(--navy-light) 0%, var(--navy) 45%, var(--navy-deep) 100%);
    display: flex;
    align-items: center;
    justify-content: center;
    gap: 16px;
  }
  .back-dot {
    width: 46px;
    height: 46px;
    border-radius: 50%;
    background: var(--orange);
  }
  .back-name {
    color: var(--orange);
    font-size: 56px;
    letter-spacing: 1px;
    text-transform: uppercase;
    line-height: 1;
  }
</style>
</head>
<body>
  <section class="card card-front">
    <svg class="decor" viewBox="0 0 520 298" width="520" height="298" aria-hidden="true">
      <circle cx="470" cy="300" r="175" fill="var(--navy)"/>
      <path d="M290 268 A183 183 0 0 1 423 123" fill="none" stroke="var(--green)" stroke-width="5" stroke-linecap="round"/>
      <text x="440" y="238" text-anchor="middle" fill="var(--orange)" font-family="Questrial, sans-serif" font-size="36">Voltrisa</text>
    </svg>
    <div class="front-info">
      <h1 class="brand-name">Voltrisa</h1>
      <p class="person-name">Mara Delgado</p>
      <ul class="contact-list">
        <li><svg viewBox="0 0 12 12"><path d="M2.5 0.5l2 2.5-1.2 1.3a7 7 0 0 0 4.4 4.4L9 7.5l2.5 2-1.3 2A9.5 9.5 0 0 1 0.5 1.8z"/></svg>+1234 8765 210</li>
        <li><svg viewBox="0 0 12 12"><path d="M0 2h12v8H0z M0.8 2.6L6 7l5.2-4.4" stroke="#fff" stroke-width="0.9"/></svg>info@voltrisa.com</li>
        <li><svg viewBox="0 0 12 12"><circle cx="6" cy="6" r="6"/></svg>www.voltrisa.com</li>
      </ul>
    </div>
    <p class="address">Havenstraat 14 B, 2311 KL Marden</p>
  </section>

  <section class="card card-back">
    <span class="back-dot" aria-hidden="true"></span>
    <h2 class="back-name">Voltrisa</h2>
  </section>
</body>
</html>
```